Letterhead and Business card for Brevon Logistics
Brevon Logistics
Letterhead and Business card for Brevon Logistics - Transportation
Creative Brief
Professional
Dirk Makhanya
Manager
17 Kolbe Street Meriton Randfontein Gauteng 1759
dirk@brevonlogistics.example

```html
<!DOCTYPE html>
<html lang="en">
<head>
<meta charset="utf-8">
<title>Brevon Logistics Stationery</title>
<link rel="stylesheet" href="https://fonts.googleapis.com/css2?family=Montserrat:wght@400;600;700&family=Dancing+Script:wght@600&display=swap">
<style>
  :root {
    --backdrop: #a9a9a9;
    --paper: #ffffff;
    --ink: #1b1b1b;
    --muted: #8a8a8a;
    --rule: #cfcfcf;
    --disc: #141414;
    --phone-body: #e9e9e9;
  }
  * { box-sizing: border-box; margin: 0; padding: 0; }
  html, body { width: 1200px; height: 350px; overflow: hidden; }
  body {
    background: var(--backdrop);
    font-family: "Montserrat", Arial, sans-serif;
    color: var(--ink);
    position: relative;
  }
  .item { position: absolute; background: var(--paper); }
  .brand { display: flex; align-items: center; gap: 4px; font-weight: 700; white-space: nowrap; }
  .brand__square { width: 9px; height: 9px; background: var(--ink); flex: none; }

  /* business cards */
  .card { left: 12px; width: 80px; height: 48px; padding: 6px; }
  .card--front { top: 233px; display: flex; align-items: center; justify-content: center; }
  .card--front .brand { font-size: 6.5px; }
  .card--back { top: 296px; font-size: 4px; line-height: 1.45; }
  .card--back .card__name { font-weight: 700; font-size: 5px; }
  .card--back .card__role { color: var(--muted); margin-bottom: 3px; }

  /* letterhead */
  .letterhead { left: 96px; top: 29px; width: 212px; height: 321px; padding: 14px 16px; font-size: 4px; line-height: 1.6; }
  .letterhead__top { display: flex; justify-content: space-between; align-items: flex-start; }
  .letterhead .brand { font-size: 8px; }
  .letterhead .brand__square { width: 10px; height: 10px; }
  .letterhead__contact { text-align: right; color: var(--muted); font-size: 3.6px; line-height: 1.5; }
  .letterhead__headline { margin-top: 18px; font-size: 9px; font-weight: 600; letter-spacing: .5px; }
  .letterhead__body p { color: var(--muted); margin-top: 6px; }
  .letterhead__sign { margin-top: 14px; color: var(--muted); }
  .letterhead__signature { font-family: "Dancing Script", cursive; font-size: 13px; color: var(--ink); line-height: 1.2; margin-top: 4px; }
  .letterhead__name { font-weight: 600; color: var(--ink); }

  /* envelopes */
  .envelope { left: 324px; width: 245px; height: 78px; }
  .envelope--back { top: 84px; overflow: hidden; }
  .envelope--front { top: 173px; padding: 12px 14px; }
  .envelope--front .brand { font-size: 8px; }
  .envelope__address { margin-top: 10px; font-size: 3.8px; color: var(--muted); line-height: 1.5; }
  .envelope__window { position: absolute; left: 120px; top: 40px; width: 100px; height: 28px; border: 1px solid var(--rule); background: #f4f4f4; }

  /* usb */
  .usb { left: 713px; top: 36px; width: 50px; height: 100px; background: none; }

  /* phone */
  .phone { left: 833px; top: 12px; width: 67px; height: 132px; border-radius: 10px; background: var(--phone-body); border: 1px solid #c4c4c4; }
  .phone__screen { position: absolute; left: 5px; top: 16px; right: 5px; bottom: 16px; background: var(--paper); border: 1px solid #d6d6d6; display: flex; align-items: center; justify-content: center; }
  .phone__screen .brand { font-size: 4.5px; }
  .phone__screen .brand__square { width: 6px; height: 6px; }

  /* notepad */
  .notepad { left: 612px; top: 150px; width: 156px; height: 150px; padding: 22px 12px; }
  .notepad__rings { position: absolute; top: -6px; left: 8px; right: 8px; height: 12px; background: repeating-linear-gradient(90deg, var(--ink) 0 3px, transparent 3px 7px); }
  .notepad .brand { font-size: 7px; justify-content: center; }

  /* disc */
  .disc { left: 1008px; top: 24px; width: 168px; height: 168px; border-radius: 50%; background: var(--disc); display: flex; align-items: center; justify-content: center; }
  .disc__hole { position: absolute; width: 22px; height: 22px; border-radius: 50%; background: var(--backdrop); border: 4px solid #2a2a2a; }
  .disc .brand { position: absolute; top: 112px; font-size: 7px; color: var(--paper); }
  .disc .brand__square { background: var(--paper); }

  /* id badge */
  .badge { left: 962px; top: 206px; width: 70px; height: 132px; padding: 10px 6px; border: 1px solid var(--rule); }
  .badge__clip { position: absolute; left: 27px; top: -30px; width: 14px; height: 34px; border: 2px solid var(--ink); border-radius: 8px 8px 2px 2px; }
  .badge__name { margin-top: 24px; font-size: 7px; font-weight: 600; text-align: center; }
  .badge__role { font-size: 4.5px; color: var(--muted); text-align: center; margin-bottom: 20px; }
  .badge .brand { font-size: 5px; justify-content: center; }
  .badge .brand__square { width: 6px; height: 6px; }
</style>
</head>
<body>

  <section class="item card card--front">
    <div class="brand"><span class="brand__square"></span>Brevon Logistics</div>
  </section>
  <section class="item card card--back">
    <div class="card__name">Dirk Makhanya</div>
    <div class="card__role">Manager</div>
    <div>17 Kolbe Street Meriton</div>
    <div>dirk@brevonlogistics.example</div>
  </section>

  <section class="item letterhead">
    <div class="letterhead__top">
      <div class="brand"><span class="brand__square"></span>Brevon Logistics</div>
      <div class="letterhead__contact">
        17 Kolbe Street Meriton<br>Randfontein Gauteng 1759<br>dirk@brevonlogistics.example
      </div>
    </div>
    <h1 class="letterhead__headline">HEADLINE</h1>
    <div class="letterhead__body">
      <p>Thank you for choosing our team for your freight needs. We move goods safely across the region every day.</p>
      <p>Our drivers and planners keep each load on time and on budget.</p>
      <p>Please contact us with any questions about your next delivery.</p>
    </div>
    <div class="letterhead__sign">
      Kind regards
      <div class="letterhead__signature">Dirk</div>
      <div class="letterhead__name">Dirk Makhanya</div>
      <div>Manager</div>
    </div>
  </section>

  <section class="item envelope envelope--back">
    <svg width="245" height="78" viewBox="0 0 245 78" aria-hidden="true">
      <rect width="245" height="78" fill="#ffffff"/>
      <path d="M0 0 L245 0 L245 14 L132 40 Q122 43 112 40 L0 14 Z" fill="#1b1b1b"/>
    </svg>
  </section>
  <section class="item envelope envelope--front">
    <div class="brand"><span class="brand__square"></span>Brevon Logistics</div>
    <div class="envelope__address">Recipient Name<br>Street Address<br>City Code</div>
    <div class="envelope__window"></div>
  </section>

  <section class="item usb">
    <svg width="50" height="100" viewBox="0 0 50 100" aria-hidden="true">
      <rect x="4" y="2" width="14" height="10" fill="#cfcfcf"/>
      <rect x="2" y="12" width="18" height="36" rx="2" fill="#1b1b1b"/>
      <rect x="26" y="58" width="18" height="38" rx="2" fill="#1b1b1b"/>
      <rect x="28" y="50" width="14" height="8" fill="#2e2e2e"/>
    </svg>
  </section>

  <section class="item phone">
    <div class="phone__screen">
      <div class="brand"><span class="brand__square"></span>Brevon Logistics</div>
    </div>
  </section>

  <section class="item notepad">
    <div class="notepad__rings"></div>
    <div class="brand"><span class="brand__square"></span>Brevon Logistics</div>
  </section>

  <section class="item disc">
    <span class="disc__hole"></span>
    <div class="brand"><span class="brand__square"></span>Brevon Logistics</div>
  </section>

  <section class="item badge">
    <span class="badge__clip"></span>
    <div class="badge__name">Dirk Makhanya</div>
    <div class="badge__role">Manager</div>
    <div class="brand"><span class="brand__square"></span>Brevon Logistics</div>
  </section>

</body>
</html>
```